QuillMark Business Cards

I need a business card designed for QuillMark. To get an idea of what we do please visit https://formvault.example/para-creadores-3

```html
<!DOCTYPE html>
<html lang="en">
<head>
<meta charset="utf-8">
<title>QuillMark Business Cards</title>
<link href="https://fonts.googleapis.com/css2?family=Montserrat:wght@400;500;600&display=swap" rel="stylesheet">
<style>
  :root {
    --ink: #1c1e22;
    --paper: #ffffff;
    --amber: #e5921c;
    --text: #1a1a1a;
    --rule: #9a9a9a;
    --backdrop: #202020;
  }
  * { box-sizing: border-box; margin: 0; padding: 0; }
  html, body { width: 1200px; height: 1015px; overflow: hidden; }
  body {
    background: var(--backdrop);
    font-family: "Montserrat", Arial, sans-serif;
    position: relative;
  }
  .card {
    position: absolute;
    left: 250px;
    width: 700px;
    height: 400px;
    overflow: hidden;
    box-shadow: 0 12px 30px rgba(0,0,0,.6);
  }
  .card-front { top: 70px; background: var(--ink); }
  .card-back { top: 545px; background: var(--paper); }

  /* brand lockup */
  .brand { position: absolute; display: flex; align-items: center; gap: 26px; }
  .brand-mark { width: 58px; height: 58px; border: 3px solid var(--amber); flex: none; }
  .brand-name {
    font-size: 40px; font-weight: 400; letter-spacing: 12px; text-transform: uppercase;
    white-space: nowrap;
  }
  .brand-sub {
    display: flex; align-items: center; gap: 10px; margin-top: 6px;
    font-size: 10px; letter-spacing: 7px; text-transform: uppercase; color: var(--amber);
    white-space: nowrap;
  }
  .brand-sub::after { content: ""; flex: 1; height: 1px; min-width: 110px; background: currentColor; opacity: .7; }
  .card-front .brand { left: 120px; top: 120px; }
  .card-front .brand-name { color: var(--paper); }
  .card-front .brand-sub::after { background: #cfcfcf; }

  .card-back .brand {
    left: 40px; top: 90px; width: 330px;
    flex-direction: column; align-items: center; gap: 22px;
  }
  .card-back .brand-text { width: 100%; }
  .card-back .brand-name { color: var(--text); font-size: 30px; letter-spacing: 8px; }
  .card-back .brand-sub { font-size: 9px; letter-spacing: 6px; }
  .card-back .brand-sub::after { background: #333; min-width: 50px; }

  .front-band {
    position: absolute; left: 0; right: 0; top: 262px; height: 44px;
    background: var(--amber); color: var(--paper);
    display: flex; align-items: center; justify-content: center;
    font-size: 17px; font-weight: 500; letter-spacing: .5px;
  }

  .divider { position: absolute; left: 395px; top: 75px; width: 1px; height: 200px; background: var(--rule); }
  .contact { position: absolute; left: 420px; top: 70px; width: 270px; color: var(--text); }
  .contact-name { font-size: 22px; font-weight: 500; color: var(--amber); text-transform: uppercase; line-height: 1.1; }
  .contact-role { font-size: 15px; margin-bottom: 16px; }
  .contact-list { list-style: none; font-size: 15px; line-height: 1.55; }
  .contact-list li { display: flex; align-items: center; gap: 9px; white-space: nowrap; }
  .contact-list svg { width: 15px; height: 15px; flex: none; }
  .accent { color: var(--amber); }
  .contact-address { font-size: 15px; line-height: 1.35; margin-top: 12px; padding-left: 24px; }

  .back-base { position: absolute; left: 0; bottom: 0; width: 700px; height: 110px; }
</style>
</head>
<body>
  <section class="card card-front">
    <div class="brand">
      <div class="brand-mark"></div>
      <div class="brand-text">
        <div class="brand-name">QuillMark</div>
        <div class="brand-sub">Digital Notary</div>
      </div>
    </div>
    <div class="front-band">www.quillmark.example</div>
  </section>

  <section class="card card-back">
    <div class="brand">
      <div class="brand-mark"></div>
      <div class="brand-text">
        <div class="brand-name">QuillMark</div>
        <div class="brand-sub">Digital Notary</div>
      </div>
    </div>
    <div class="divider"></div>
    <div class="contact">
      <div class="contact-name">Daniel Porter</div>
      <div class="contact-role">Managing Director</div>
      <ul class="contact-list">
        <li><svg viewBox="0 0 16 16"><path fill="#e5921c" d="M3 1l3 3-2 2c1 2 3 4 5 5l2-2 3 3-2 3C6 14 2 10 1 3z"/></svg><span>044-555 010 234</span></li>
        <li><svg viewBox="0 0 16 16"><rect x="1" y="3" width="14" height="10" fill="#e5921c"/><path d="M1 3l7 6 7-6" fill="none" stroke="#fff" stroke-width="1.4"/></svg><span>info@quillmark.example</span></li>
        <li><svg viewBox="0 0 16 16"><circle cx="8" cy="8" r="7" fill="#e5921c"/><path d="M1 8h14M8 1v14M3 4.5h10M3 11.5h10" stroke="#fff" stroke-width="1"/><ellipse cx="8" cy="8" rx="3" ry="7" fill="none" stroke="#fff" stroke-width="1"/></svg><span>www.<span class="accent">quillmark</span>.example</span></li>
      </ul>
      <div class="contact-address">421, Address line goes here<br>45452, Country Name</div>
    </div>
    <svg class="back-base" viewBox="0 0 700 110" preserveAspectRatio="none">
      <polygon points="0,92 430,92 430,110 0,110" fill="#e5921c"/>
      <polygon points="430,18 700,18 700,110 436,110" fill="#1c1e22"/>
    </svg>
  </section>
</body>
</html>
```